Luxury Candle Startup Needs Modern Packaging Box & Matching Label Design

We are Lunavale, a luxury candle company about to launch in Australia and we need a box packaging design that is modern, minimalist, and feminine. Our target audience are females, mostly mothers, within the age range of 25-45 who are looking for high quality, handmade luxurious products. Our company is going to have a large social media presence with new mothers as we are going to show our journey with starting a business whilst on maternity leave. We would like the arch shape incorporated into the box packaging as it is beautiful and symbolises moving into a new phase in life which really represents the brand. We would like for the packaging box to be a simple white box with a sleeve insert over the box with the design to make printing easier. Our colour inspiration are very earthy colours and would like the sleeve colour to be easily changed according to the scent. For example dusky rose coloured sleeve for rose patchouli and amber scent, light coffee coloured sleeve for coffee bean cacao scent etc. Please see uploaded files for inspiration, our logo, and the type of candle jars used.
The box dimensions are:
External Dimension: 95mmW x 95mmL x 116mmH
We look forward to seeing your amazing designs!

```html
<!DOCTYPE html>
<html lang="en">
<head>
<meta charset="utf-8">
<title>Lunavale – Candle Box Sleeves</title>
<link rel="stylesheet" href="https://fonts.googleapis.com/css2?family=Italiana&family=Montserrat:wght@500&family=Roboto:wght@400&display=swap">
<style>
  :root {
    --canvas: #f7f7f7;
    --box-white: #ffffff;
    --box-edge: #e6e6e6;
    --sleeve-cream: #ede2d6;
    --ink: #1f1a17;
    --coffee-grey: #c2c2c2;
    --coffee-latte: #dfb894;
    --coffee-roast: #904d24;
    --rose-sage: #bccbc0;
    --rose-dusk: #e3b8a8;
    --rose-terracotta: #d27e64;
  }
  * { box-sizing: border-box; margin: 0; padding: 0; }
  html, body { width: 1200px; height: 1200px; overflow: hidden; }
  body {
    background: var(--canvas);
    position: relative;
  }
  .box-face {
    position: absolute;
    top: 330px;
    width: 440px;
    height: 537px;
    background: var(--box-white);
    border: 1px solid var(--box-edge);
  }
  .box-face--coffee { left: 120px; }
  .box-face--rose { left: 640px; }
  .sleeve {
    position: absolute;
    left: 90px;
    top: 0;
    width: 260px;
    height: 100%;
    background: var(--sleeve-cream);
  }
  .arch {
    position: absolute;
    left: 10px;
    top: 30px;
    width: 240px;
    height: 507px;
    border-radius: 120px 120px 0 0;
  }
  .box-face--coffee .arch {
    background: linear-gradient(180deg, var(--coffee-grey) 0%, var(--coffee-latte) 22%, var(--coffee-latte) 65%, var(--coffee-roast) 100%);
  }
  .box-face--rose .arch {
    background: linear-gradient(180deg, var(--rose-sage) 0%, var(--rose-dusk) 30%, var(--rose-dusk) 70%, var(--rose-terracotta) 100%);
  }
  .brand {
    position: absolute;
    left: 0;
    top: 230px;
    width: 100%;
    text-align: center;
    color: var(--ink);
  }
  .brand__name {
    font-family: "Italiana", serif;
    font-size: 40px;
    letter-spacing: 2px;
    text-transform: uppercase;
    line-height: 1;
  }
  .brand__tagline {
    font-family: "Montserrat", sans-serif;
    font-weight: 500;
    font-size: 7px;
    letter-spacing: 1.5px;
    margin-top: 10px;
    line-height: 1.9;
  }
  .scent {
    position: absolute;
    left: 0;
    top: 390px;
    width: 100%;
    text-align: center;
    font-family: "Roboto", sans-serif;
    font-size: 18px;
    line-height: 1.25;
    color: var(--ink);
  }
</style>
</head>
<body>
  <section class="box-face box-face--coffee">
    <div class="sleeve">
      <div class="arch" role="img" aria-label="Abstract organic shapes in grey, latte and roasted brown with small coffee bean motifs"></div>
      <div class="brand">
        <p class="brand__name">Lunavale</p>
        <p class="brand__tagline">LUXURY FRAGRANCE<br>AUSTRALIA</p>
      </div>
      <p class="scent">Coffee Bean<br>&amp; Cacao</p>
    </div>
  </section>

  <section class="box-face box-face--rose">
    <div class="sleeve">
      <div class="arch" role="img" aria-label="Abstract organic shapes in sage green, dusky rose, terracotta and cream"></div>
      <div class="brand">
        <p class="brand__name">Lunavale</p>
        <p class="brand__tagline">LUXURY FRAGRANCE<br>AUSTRALIA</p>
      </div>
      <p class="scent">Rose Patchouli<br>&amp; Amber</p>
    </div>
  </section>
</body>
</html>
```